Martial Arts Website

Redevelopment of existing martial arts website.

The academy teaches traditional shaolin martial arts, including Shaolin Kung Fu, Wu Shu, Tai Chi, Qigong and Wing Chun and the site needs to reflect the traditional roots (eg, no tacky boxing imagery)

Existing website is www.copperheron.com.au to get a feel for the desired color scheme (black, green and red). The exact colors can be tweaked though. Please only reuse the logo and font (Karate) - there isnt anything else from the current design that needs to remain.

The current website includes links to a ViewTube channel that includes demonstrations of the training conducted to better guide the design.

The new website site map will be:
1. Home
2. Programs - summary page describing each form of training
a. Tiny Otters
b. Kids Kung Fu
c. Youth Kung Fu
d. Adults Kung Fu
e. Wing Chun
f. Tai Chi & Qigong
g. Weaponry Classes
h. 72 Arts of Shaolin Conditioning Program
i. Acrobatics and Wu Shu
j. Fitness Boxing
3. Timetable
4. Coaches - summary page describing all coaches
a. Sifu (Master)
b. Sihing Lou
c. Sihing Kim
d. Sihing Felix
X. ... up to 10 or so coaches
5. Member Zone
6. Contact Us
Updates

Logo now attached to brief - sorry I only have it in PDF

Just to clarify, I am only expecting a PSD design - no HTML required

Reason: Thanks for the designs, we love a lot of them just require a little extra time to tweak the designs and establish the potential. Thanks for your understanding and efforts.

Target Market(s)

Parents, teenagers, young adults, adults, elderly

Industry/Entity Type

Training

Requirements
Must have
• Chinese kung fu dragon imagery throughout the background
Links to Circlebook and ViewTube channel
Promo/icon in the header "Try 2 free classes now"
Home page should include an embedded ViewTube video

```html
<!DOCTYPE html>
<html lang="en">
<head>
<meta charset="utf-8">
<title>Copper Heron Martial Arts Academy</title>
<link href="https://fonts.googleapis.com/css2?family=Arimo:ital,wght@0,400;0,700;1,400&family=Macondo+Swash+Caps&family=Open+Sans:wght@400&display=swap" rel="stylesheet">
<style>
  :root {
    --page-side: #1b1b1b;
    --page: #000000;
    --panel: #0b0b0b;
    --panel-line: #202020;
    --sidebar: #191919;
    --brand-green: #5cd02a;
    --brand-ring: #3fae1f;
    --tagline-green: #3f8a1f;
    --nav-top: #86c21c;
    --nav-bottom: #3b6a08;
    --nav-active: #86e81e;
    --nav-text: #16240a;
    --heading: #d6d6d6;
    --class-link: #8f8f8f;
    --body-text: #6a8455;
    --more-link: #5d7a45;
    --footer: #1f4f94;
    --dragon-blue: #1a3fd0;
    --dragon-deep: #0a1a6e;
    --robe-orange: #c98420;
    --robe-blue: #3a6aa8;
  }
  * { box-sizing: border-box; margin: 0; padding: 0; }
  html, body { width: 1015px; height: 1200px; overflow: hidden; }
  body {
    position: relative;
    background: linear-gradient(to bottom, var(--page-side) 0, var(--page-side) 592px, var(--page) 592px);
    font-family: "Open Sans", sans-serif;
  }
  .site { position: absolute; left: 65px; top: 0; width: 886px; height: 1200px; background: var(--page); }

  /* header */
  .brand-mark {
    position: absolute; left: 2px; top: 16px; width: 92px; height: 92px;
    border-radius: 50%; background: var(--brand-ring);
  }
  .brand-name {
    position: absolute; left: 104px; top: 68px;
    font-family: "Arimo", sans-serif; font-weight: 700; font-size: 43px;
    color: var(--brand-green); white-space: nowrap;
  }
  .tagline {
    position: absolute; left: 421px; top: 132px;
    font-family: "Arimo", sans-serif; font-style: italic; font-size: 15px; color: var(--tagline-green);
  }
  .promo-badge {
    position: absolute; left: 503px; top: -6px; width: 120px; height: 70px;
    border-radius: 0 0 60px 60px / 0 0 45px 45px;
    background: linear-gradient(#7fd33e, #3e9a18);
    border: 4px solid #e8f3e2;
    color: #eaf7e0; font-family: "Arimo", sans-serif; font-size: 12px; line-height: 14px;
    text-align: center; padding-top: 12px;
  }
  .hero-art {
    position: absolute; left: 40px; top: 165px; width: 780px; height: 427px;
    background:
      radial-gradient(ellipse 130px 210px at 660px 220px, rgba(58,106,168,0.85) 0%, rgba(58,106,168,0.3) 60%, transparent 100%),
      radial-gradient(ellipse 200px 120px at 650px 80px, rgba(201,132,32,0.9) 0%, rgba(201,132,32,0.35) 60%, transparent 100%),
      radial-gradient(ellipse 260px 260px at 250px 230px, var(--dragon-blue) 0%, var(--dragon-deep) 55%, transparent 100%),
      linear-gradient(90deg, #050c30 0%, #030818 45%, #000 55%, #0a0d18 80%, #000 100%);
  }

  /* navigation */
  .main-nav {
    position: absolute; left: 0; top: 592px; width: 886px; height: 65px;
    background: linear-gradient(var(--nav-top), var(--nav-bottom));
  }
  .nav-item {
    position: absolute; top: 0; height: 65px; line-height: 65px;
    font-family: "Arimo", sans-serif; font-weight: 700; font-size: 16px;
    color: var(--nav-text); text-shadow: 0 1px 0 rgba(255,255,255,0.35);
    transform: translateX(-50%); white-space: nowrap;
  }
  .nav-item.is-active {
    left: 174px !important; width: 118px; text-align: center; transform: none;
    background: linear-gradient(var(--nav-active), #5cc010); border-left: 1px solid #9ff04a; border-right: 1px solid #9ff04a;
  }

  /* sidebar */
  .class-list {
    position: absolute; left: 0; top: 658px; width: 209px; height: 320px;
    background: var(--sidebar);
  }
  .section-title {
    font-family: "Macondo Swash Caps", cursive; font-size: 22px; color: var(--heading);
    text-shadow: 0 1px 2px #000;
  }
  .class-list .section-title { position: absolute; left: 42px; top: 22px; }
  .class-list .rule { position: absolute; left: 42px; top: 54px; width: 128px; height: 1px; background: #555; }
  .class-link {
    position: absolute; left: 42px; font-family: "Arimo", sans-serif; font-size: 15px; color: var(--class-link);
  }
  .social-box {
    position: absolute; left: 0; top: 985px; width: 209px; height: 123px;
    background: var(--panel); border: 1px solid var(--panel-line);
  }
  .social-link {
    position: absolute; top: 52px; font-family: "Arimo", sans-serif; font-size: 14px; color: #9a9a9a;
    transform: translateX(-50%);
  }

  /* content panels */
  .panel {
    position: absolute; background: var(--panel); border: 1px solid var(--panel-line); border-radius: 4px;
  }
  .panel .section-title { position: absolute; left: 25px; top: 10px; }
  .about { left: 239px; top: 681px; width: 647px; height: 185px; }
  .about p {
    position: absolute; left: 25px; top: 50px; width: 596px;
    font-size: 12px; line-height: 13.3px; color: var(--body-text); letter-spacing: 0.15px;
  }
  .more-link {
    position: absolute; right: 30px; font-size: 12px; color: var(--more-link); letter-spacing: 0.3px;
  }
  .about .more-link { top: 151px; }
  .news { left: 239px; top: 889px; width: 312px; height: 220px; }
  .news-item { position: absolute; left: 25px; width: 270px; }
  .news-icon { position: absolute; left: 0; top: 2px; }
  .news-item p {
    margin-left: 43px; width: 220px; font-size: 12px; line-height: 13.4px; color: var(--body-text);
  }
  .news .more-link { top: 201px; right: 20px; }
  .video { left: 577px; top: 888px; width: 309px; height: 221px; }
  .video-player { position: absolute; left: 29px; top: 43px; width: 246px; height: 140px; background: #050505; }
  .video-still {
    position: absolute; left: 58px; top: 6px; width: 121px; height: 120px;
    background: linear-gradient(#6a5a6a, #a0566a 70%, #8a3a4a);
  }
  .video-channel { position: absolute; right: 6px; top: 108px; font-family: "Arimo", sans-serif; font-size: 11px; color: #bbb; }
  .video-controls { position: absolute; left: 0; bottom: 0; width: 246px; height: 13px; background: linear-gradient(#eee, #bbb); }
  .video .more-link { top: 203px; right: 16px; }

  .site-footer {
    position: absolute; left: 0; top: 1157px; width: 886px; text-align: center;
    font-size: 12px; color: var(--footer); letter-spacing: 0.3px;
  }
</style>
</head>
<body>
<div class="site">
  <header>
    <div class="brand-mark"></div>
    <div class="brand-name">Copper Heron Martial Arts Academy</div>
    <div class="tagline">Traditional kung fu &amp; tai chi center</div>
    <div class="promo-badge">Try 2 free<br>classes now</div>
    <div class="hero-art" role="img" aria-label="Glowing blue Chinese dragon beside a kung fu master in orange and blue robes performing a high kick"></div>
  </header>

  <nav class="main-nav">
    <span class="nav-item is-active">HOME</span>
    <span class="nav-item" style="left:353px">ABOUT US</span>
    <span class="nav-item" style="left:470px">TIME TABLE</span>
    <span class="nav-item" style="left:586px">MEMBERS</span>
    <span class="nav-item" style="left:705px">CONTACTS</span>
  </nav>

  <aside class="class-list">
    <h2 class="section-title">Classes</h2>
    <div class="rule"></div>
    <a class="class-link" style="top:61px">Tiny Otters</a>
    <a class="class-link" style="top:86px">Kids Kung Fu</a>
    <a class="class-link" style="top:110px">Youth Kung Fu</a>
    <a class="class-link" style="top:136px">Adults Kung Fu</a>
    <a class="class-link" style="top:161px">Wing Chun</a>
    <a class="class-link" style="top:190px">Tai Chi &amp; Qigong</a>
    <a class="class-link" style="top:216px">Weaponry Classes</a>
    <a class="class-link" style="top:244px">72 Arts of Shaolin</a>
    <a class="class-link" style="top:269px">Performance Team</a>
  </aside>

  <div class="social-box">
    <a class="social-link" style="left:53px">Circlebook</a>
    <a class="social-link" style="left:143px">ViewTube</a>
  </div>

  <section class="panel about">
    <h2 class="section-title">About Us</h2>
    <p>Lorem ipsum dolor sit amet, consectetuer adipiscing elit. Aenean commodo ligula eget dolor. Aenean massa. Cum sociis natoque penatibus et magnis dis parturient montes, nascetur ridiculus mus. Donec quam felis, ultricies nec, pellentesque eu, pretium quis, sem. Nulla consequat massa quis enim. Donec pede justo, fringilla vel, aliquet nec, vulputate eget, arcu. In enim justo, rhoncus ut, imperdiet a, venenatis vitae, justo. Nullam dictum felis eu pede mollis pretium. Integer tincidunt. Cras dapibus. Vivamus elementum semper nisi. Aenean vulputate eleifend tellus. Aenean leo ligula, porttitor eu, consequat vitae, eleifend ac, enim. Aliquam lorem ante, dapibus in, viverra quis, feugiat a, tellus.</p>
    <a class="more-link">READ MORE!</a>
  </section>

  <section class="panel news">
    <h2 class="section-title">News &amp; Updates</h2>
    <div class="news-item" style="top:48px">
      <svg class="news-icon" width="36" height="30" viewBox="0 0 36 30"><line x1="3" y1="3" x2="33" y2="27" stroke="#aaa" stroke-width="3" stroke-linecap="round"/></svg>
      <p>Lorem ipsum dolor sit amet, consectetuer adipiscing elit. Aenean commodo ligula eget dolor. Aenean</p>
    </div>
    <div class="news-item" style="top:103px">
      <svg class="news-icon" width="36" height="30" viewBox="0 0 36 30"><line x1="3" y1="3" x2="33" y2="27" stroke="#aaa" stroke-width="3" stroke-linecap="round"/></svg>
      <p>Lorem ipsum dolor sit amet, consectetuer adipiscing elit. Aenean commodo ligula eget dolor. Aenean</p>
    </div>
    <div class="news-item" style="top:154px">
      <svg class="news-icon" width="36" height="30" viewBox="0 0 36 30"><line x1="3" y1="3" x2="33" y2="27" stroke="#aaa" stroke-width="3" stroke-linecap="round"/></svg>
      <p>Lorem ipsum dolor sit amet, consectetuer adipiscing elit. Aenean commodo ligula eget dolor. Aenean</p>
    </div>
    <a class="more-link">MORE NEWS!</a>
  </section>

  <section class="panel video">
    <h2 class="section-title">Latest Video</h2>
    <div class="video-player">
      <div class="video-still" role="img" aria-label="Video still of young students in white uniforms"></div>
      <svg style="position:absolute;left:101px;top:52px" width="40" height="26" viewBox="0 0 40 26"><rect x="0.5" y="0.5" width="39" height="25" rx="6" fill="#ddd" stroke="#999"/><path d="M16 7 L27 13 L16 19 Z" fill="#444"/></svg>
      <span class="video-channel">ViewTube</span>
      <div class="video-controls">
        <svg width="246" height="13" viewBox="0 0 246 13"><path d="M6 3 L12 6.5 L6 10 Z" fill="#333"/><rect x="22" y="5" width="140" height="3" fill="#888"/><circle cx="26" cy="6.5" r="3" fill="#666"/><text x="170" y="9.5" font-size="7" font-family="Arimo, sans-serif" fill="#333">0:00 / 0:00</text></svg>
      </div>
    </div>
    <a class="more-link">MORE Videos!</a>
  </section>

  <footer class="site-footer">Copyright © 2012 - Copper Heron Martial Arts Pty Ltd. Westbrook NSW 2790</footer>
</div>
</body>
</html>
```